Velmora Biz Card 2019

New business card for Velmora Property Inspections. We are a residential home inspection company in Arizona.

Target Market(s)

Real Estate

Font styles to use
Sans Serif

Requirements
Must have
• Glen Mirewick
• Home Inspector
• Velmora Property Inspections, LLC
• 480-555-0172
• glen@velmora-llc.example

```html
<!DOCTYPE html>
<html lang="en">
<head>
<meta charset="utf-8">
<title>Velmora Property Inspections – Business Card</title>
<link rel="stylesheet" href="https://fonts.googleapis.com/css2?family=Open+Sans:wght@400;600&family=Raleway:wght@300;700&display=swap">
<style>
  :root {
    --canvas: #dcdcdc;
    --card-white: #ffffff;
    --card-black: #1c1c1c;
    --green: #3dae3f;
    --ink: #4a4a4a;
    --ink-dark: #333333;
    --grey-mark: #8a8a8a;
    --shirt-navy: #27324a;
    --photo-light: #eef0f3;
  }
  * { box-sizing: border-box; margin: 0; padding: 0; }
  html, body { width: 1200px; height: 900px; overflow: hidden; }
  body {
    background: var(--canvas);
    font-family: "Open Sans", Arial, sans-serif;
    position: relative;
  }
  .card {
    position: absolute;
    left: 280px;
    width: 640px;
    height: 366px;
    border-radius: 30px;
    overflow: hidden;
    box-shadow: 0 10px 24px rgba(0,0,0,0.18);
  }
  .card--front { top: 64px; background: var(--card-white); }
  .card--back { top: 474px; background: var(--card-black); }

  .portrait {
    position: absolute;
    left: 0; top: 40px;
    width: 300px; height: 268px;
    background: linear-gradient(180deg, var(--photo-light) 0%, #c9ccd3 38%, var(--shirt-navy) 62%, var(--shirt-navy) 100%);
  }
  .web-band {
    position: absolute;
    left: 0; right: 0; bottom: 0;
    height: 58px;
    background: var(--green);
    color: #fff;
    font-size: 22px;
    letter-spacing: 4px;
    text-align: right;
    padding: 13px 40px 0 0;
  }
  .identity {
    position: absolute;
    right: 40px; top: 52px;
    text-align: right;
    font-family: "Raleway", Arial, sans-serif;
  }
  .identity__name {
    font-size: 28px;
    color: var(--ink-dark);
    letter-spacing: -0.5px;
  }
  .identity__first { font-weight: 700; }
  .identity__last { font-weight: 300; }
  .identity__role {
    font-size: 21px;
    font-weight: 300;
    color: var(--green);
    margin-top: 2px;
  }
  .identity__rule {
    display: block;
    width: 80px; height: 3px;
    background: var(--green);
    margin: 16px 0 0 auto;
  }
  .contact {
    position: absolute;
    right: 40px; top: 182px;
    list-style: none;
    text-align: right;
    font-size: 18px;
    line-height: 27px;
    color: var(--ink);
  }
  .contact__item {
    display: flex;
    align-items: center;
    justify-content: flex-end;
    gap: 12px;
  }
  .contact__icon { width: 22px; height: 22px; flex: none; }
  .contact__icon--blank { visibility: hidden; }

  .brand {
    position: absolute;
    left: 0; right: 0; top: 128px;
    text-align: center;
  }
  .brand__name {
    display: inline-flex;
    align-items: center;
    gap: 14px;
    font-size: 54px;
    font-weight: 600;
    color: var(--grey-mark);
    letter-spacing: 1px;
  }
  .brand__square {
    width: 26px; height: 26px;
    background: var(--green);
  }
  .brand__tagline {
    margin-top: 8px;
    font-size: 15px;
    letter-spacing: 5px;
    color: var(--green);
    text-transform: uppercase;
  }
</style>
</head>
<body>

<section class="card card--front" aria-label="Business card front">
  <div class="portrait" role="img" aria-label="Portrait photo of the inspector in a navy company polo shirt"></div>

  <div class="identity">
    <p class="identity__name"><span class="identity__first">GLEN</span> <span class="identity__last">MIREWICK</span></p>
    <p class="identity__role">Home Inspector</p>
    <span class="identity__rule"></span>
  </div>

  <ul class="contact">
    <li class="contact__item"><span>4410 S. Larkin St.</span>
      <svg class="contact__icon contact__icon--blank" viewBox="0 0 24 24"></svg></li>
    <li class="contact__item"><span>Corlan, AZ 85099</span>
      <svg class="contact__icon" viewBox="0 0 24 24"><path fill="#3dae3f" d="M12 2a7 7 0 0 0-7 7c0 5 7 13 7 13s7-8 7-13a7 7 0 0 0-7-7zm0 9.5A2.5 2.5 0 1 1 12 6.5a2.5 2.5 0 0 1 0 5z"/></svg></li>
    <li class="contact__item"><span>480-555-0172</span>
      <svg class="contact__icon" viewBox="0 0 24 24"><path fill="#3dae3f" d="M6.6 10.8a15 15 0 0 0 6.6 6.6l2.2-2.2a1 1 0 0 1 1-.25 11.4 11.4 0 0 0 3.6.57 1 1 0 0 1 1 1V20a1 1 0 0 1-1 1A17 17 0 0 1 3 4a1 1 0 0 1 1-1h3.5a1 1 0 0 1 1 1c0 1.25.2 2.45.57 3.57a1 1 0 0 1-.25 1z"/></svg></li>
    <li class="contact__item"><span>glen@velmora-llc.example</span>
      <svg class="contact__icon" viewBox="0 0 24 24"><rect x="2" y="5" width="20" height="14" fill="none" stroke="#3dae3f" stroke-width="2"/><path d="M2 5l10 8 10-8" fill="none" stroke="#3dae3f" stroke-width="2"/></svg></li>
  </ul>

  <div class="web-band">velmora-llc.example</div>
</section>

<section class="card card--back" aria-label="Business card back">
  <div class="brand">
    <p class="brand__name"><span class="brand__square"></span>VELMORA</p>
    <p class="brand__tagline">Property Inspections, LLC</p>
  </div>
</section>

</body>
</html>
```